DM - management consultant

Business card - contemporary design

Front info
Dorian Maples

(Address not necessary)
PO Box 7386
Belmont, CA 94002

(650) 555-0143
dm@dorianmapl.es

Twitter: dmq527
Facebook: /Dorian.Maples
Linkedin: /in/dorianmaples

Back or Front
www.dorianmaples.net
Facilitation & coaching, change management, strategic partnerships, business improvement

Target Market(s)

High tech businesses - mostly startups in Silicon Valley

Industry/Entity Type

Business

Font styles to use
Sans Serif

Colors

Designer to choose colors to be used in the design.

```html
<!DOCTYPE html>
<html lang="en">
<head>
<meta charset="utf-8">
<title>Dorian Maples – Business Card</title>
<link rel="stylesheet" href="https://fonts.googleapis.com/css2?family=Cinzel:wght@400;500&family=Lato:wght@400;700&display=swap">
<style>
  :root {
    --backdrop: #d9d4cc;
    --card: #1d1d1f;
    --card-edge: #2a2a2d;
    --teal: #1fb3bf;
    --teal-deep: #0f7f89;
    --ink-light: #d8d8d8;
    --ink-soft: #b9b9b9;
    --mark-faint: #2c3c3e;
  }
  * { margin: 0; padding: 0; box-sizing: border-box; }
  html, body {
    width: 1200px; height: 1000px; overflow: hidden;
    background: var(--backdrop);
  }
  .canvas {
    position: relative; width: 1200px; height: 1000px;
    display: flex; flex-direction: column; align-items: center; justify-content: center; gap: 60px;
  }
  .card {
    position: relative; width: 700px; height: 400px;
    background: var(--card);
    border: 1px solid var(--card-edge);
    border-radius: 18px;
    overflow: hidden;
    box-shadow: 0 10px 24px rgba(0,0,0,.25);
    font-family: "Lato", sans-serif;
  }
  .teal-text {
    background: linear-gradient(180deg, var(--teal) 0%, var(--teal-deep) 100%);
    -webkit-background-clip: text; background-clip: text; color: transparent;
  }
  .monogram {
    font-family: "Lato", sans-serif; font-weight: 700; color: var(--teal);
    letter-spacing: 2px; line-height: 1;
  }

  /* Front */
  .card-front { text-align: center; }
  .card-front .monogram { position: absolute; top: 62px; left: 0; right: 0; font-size: 62px; }
  .card-front .brand-name {
    position: absolute; top: 150px; left: 0; right: 0;
    font-family: "Cinzel", serif; font-weight: 500; font-size: 46px; letter-spacing: 1px;
  }
  .card-front .services {
    position: absolute; top: 218px; left: 0; right: 0;
    font-size: 19px; line-height: 1.4; color: var(--ink-soft); letter-spacing: .8px;
  }
  .card-front .website {
    position: absolute; bottom: 44px; left: 0; right: 0;
    font-size: 19px; font-weight: 700; letter-spacing: 3px; color: var(--teal-deep);
  }

  /* Back */
  .card-back .header {
    position: absolute; top: 26px; left: 48px;
    display: flex; align-items: baseline; gap: 22px;
  }
  .card-back .header .monogram { font-size: 40px; }
  .card-back .header .brand-name {
    font-family: "Cinzel", serif; font-weight: 500; font-size: 38px; letter-spacing: 1px;
  }
  .card-back .person {
    position: absolute; top: 118px; left: 48px;
    font-family: "Cinzel", serif; font-size: 30px; letter-spacing: 2px; color: var(--teal-deep);
  }
  .contact-list {
    position: absolute; top: 190px; left: 48px; list-style: none;
  }
  .contact-list li {
    display: flex; align-items: center; gap: 10px;
    font-size: 19px; color: var(--ink-light); letter-spacing: .6px; height: 25px;
  }
  .contact-list svg { width: 18px; height: 18px; fill: var(--teal); flex: none; }
  .contact-list .marker { width: 14px; height: 14px; background: var(--teal); margin: 0 2px; flex: none; }
  .card-back .address {
    position: absolute; top: 348px; left: 48px;
    font-size: 19px; color: var(--ink-light); letter-spacing: .4px;
  }
  .card-back .watermark {
    position: absolute; right: 52px; bottom: 40px;
    font-family: "Lato", sans-serif; font-weight: 700; font-size: 130px; line-height: 1;
    color: var(--mark-faint); letter-spacing: 4px;
  }
</style>
</head>
<body>
<main class="canvas">
  <section class="card card-front" aria-label="Card front">
    <div class="monogram">DM</div>
    <h1 class="brand-name teal-text">DORIAN MAPLES</h1>
    <p class="services">Facilitation &amp; Coaching, Change Management,<br>Strategic Partnerships, Business Improvement.</p>
    <p class="website">www.dorianmaples.net</p>
  </section>

  <section class="card card-back" aria-label="Card back">
    <div class="header">
      <span class="monogram">DM</span>
      <span class="brand-name teal-text">DORIAN MAPLES</span>
    </div>
    <h2 class="person">Dorian Maples</h2>
    <ul class="contact-list">
      <li>
        <svg viewBox="0 0 24 24" aria-hidden="true"><path d="M6.6 10.8a15.1 15.1 0 0 0 6.6 6.6l2.2-2.2c.3-.3.7-.4 1-.2 1.1.4 2.3.6 3.6.6.6 0 1 .4 1 1V20c0 .6-.4 1-1 1A17 17 0 0 1 3 4c0-.6.4-1 1-1h3.5c.6 0 1 .4 1 1 0 1.3.2 2.5.6 3.6.1.3 0 .7-.2 1z"/></svg>
        (650) 555-0143
      </li>
      <li>
        <svg viewBox="0 0 24 24" aria-hidden="true"><path d="M2 5h20v2l-10 6L2 7z"/><path d="M2 9l10 6 10-6v10H2z"/></svg>
        dm@dorianmapl.es
      </li>
      <li><span class="marker" aria-hidden="true"></span>dmq527</li>
      <li><span class="marker" aria-hidden="true"></span>/Dorian.Maples</li>
      <li><span class="marker" aria-hidden="true"></span>/in/dorianmaples</li>
    </ul>
    <p class="address">P.O. Box 7386 Belmont, CA 94002</p>
    <div class="watermark" aria-hidden="true">DM</div>
  </section>
</main>
</body>
</html>
```